Double Sided Flyer for 3D printing services company

We need a nice balanced flyer for our corporate handout. The attached is for concept only and not the final design. We think the attached examples have elements that balance nicely but the graphics are not good. We are attaching the logo from the corporate office for our new logo. We will add the company information after the final design is selected for web address, phone, mailing etc. Please leave room for that information in the design. Please ask any questions prior to submission. Our main focus is printing RUBBER 3D Parts and not plastic parts. The images selected should be focused on that. We also need to ensure the images are approved for use in a corporate flyer for content.

```html
<!DOCTYPE html>
<html lang="en">
<head>
<meta charset="utf-8">
<title>Nova Forge – 3D Printing Services Flyer</title>
<link href="https://fonts.googleapis.com/css2?family=Montserrat:wght@400;500;600;700;800;900&display=swap" rel="stylesheet">
<style>
  :root{
    --orange:#e0672a;
    --orange-dark:#c2531c;
    --charcoal:#474747;
    --grey:#6d6d6d;
    --light:#f1f1f1;
    --bg:#e9e9e9;
    --white:#ffffff;
    --photo-a:#8e98a3;
    --photo-b:#d9dde1;
  }
  *{box-sizing:border-box;margin:0;padding:0}
  html,body{width:882px;height:1200px;overflow:hidden;background:var(--bg);font-family:"Montserrat",Arial,sans-serif;color:var(--charcoal)}
  .sheet{position:absolute;top:303px;width:420px;height:594px;background:var(--white);overflow:hidden;box-shadow:0 2px 8px rgba(0,0,0,.12)}
  .sheet--front{left:14px}
  .sheet--back{left:448px}

  /* front */
  .brand{position:absolute;top:16px;left:18px;display:flex;align-items:center;gap:6px;font-weight:800;font-size:15px;color:var(--charcoal);letter-spacing:.5px}
  .brand__mark{width:16px;height:16px;background:var(--orange)}
  .hero-ring{position:absolute;top:0;left:150px;width:290px;height:300px}
  .hero-photo{position:absolute;top:36px;left:190px;width:212px;height:212px;border-radius:50%;background:radial-gradient(circle at 45% 40%,#e9e2da 0%,#b9b3ad 45%,#5a5f66 100%)}
  .headline{position:absolute;top:118px;left:16px;line-height:.9}
  .headline__big{font-size:92px;font-weight:900;color:var(--charcoal);letter-spacing:-3px}
  .headline__sub{font-size:38px;font-weight:900;color:var(--orange);letter-spacing:-1px}
  .samples{position:absolute;top:328px;left:24px;right:24px;display:flex;justify-content:space-between}
  .sample{width:82px;height:82px;border-radius:50%;border:5px solid var(--light);box-shadow:0 0 0 2px #bdbdbd}
  .sample:nth-child(1){background:radial-gradient(circle,#c23a2a,#3b3b3b)}
  .sample:nth-child(2){background:radial-gradient(circle,#9aa2aa,#4a4f55)}
  .sample:nth-child(3){background:radial-gradient(circle,#e7e1d8,#7c7670)}
  .sample:nth-child(4){background:radial-gradient(circle,#cfd6dc,#5d6670)}
  .features{position:absolute;top:436px;left:0;right:0;height:98px;background:var(--orange);display:flex;justify-content:space-around;align-items:center;padding:0 12px}
  .feature{display:flex;align-items:center;gap:7px;width:122px}
  .feature__icon{flex:none;width:34px;height:34px;border-radius:50%;border:2px solid var(--white);display:flex;align-items:center;justify-content:center}
  .feature__text{font-size:8px;font-weight:700;color:var(--white);line-height:1.3;text-transform:uppercase}
  .contact{position:absolute;bottom:0;left:0;right:0;height:60px;display:flex;justify-content:space-between;align-items:center;padding:0 22px;font-size:12px;font-weight:800;color:var(--orange)}
  .contact__item{display:flex;align-items:center;gap:6px}
  .contact__web{font-size:9px;font-weight:600;color:var(--grey)}

  /* back */
  .intro{position:absolute;top:22px;left:22px;right:22px}
  .intro__title{font-size:24px;font-weight:800;line-height:1.1;color:var(--orange)}
  .intro__title span{color:var(--charcoal)}
  .intro__copy{margin-top:8px;font-size:7.5px;line-height:1.45;color:var(--grey);width:330px}
  .checklist{position:absolute;top:132px;left:22px;list-style:none;z-index:2}
  .checklist li{display:flex;align-items:center;gap:5px;font-size:7.5px;color:var(--charcoal);margin-bottom:3px}
  .checklist svg{flex:none}
  .wide-photo{position:absolute;top:120px;left:0;right:0;height:140px;background:linear-gradient(180deg,var(--white) 0%,rgba(255,255,255,0) 45%),linear-gradient(90deg,var(--photo-b) 0%,var(--photo-a) 60%,#c98e74 100%)}
  .benefits__title{position:absolute;top:276px;left:22px;font-size:20px;font-weight:800;color:var(--orange)}
  .benefits__title span{color:var(--charcoal)}
  .benefits{position:absolute;top:312px;left:22px;right:22px;list-style:none}
  .benefit{display:flex;gap:12px;align-items:center;height:58px}
  .benefit__icon{flex:none;width:40px;height:40px;border-radius:50%;border:2px solid var(--orange);display:flex;align-items:center;justify-content:center}
  .benefit__title{font-size:11px;font-weight:800;color:var(--orange)}
  .benefit__text{font-size:7.5px;line-height:1.4;color:var(--grey);margin-top:2px}
  .footer-bar{position:absolute;bottom:0;left:0;right:0;height:38px;background:var(--orange);display:flex;justify-content:space-between;align-items:center;padding:0 22px;color:var(--white);font-size:11px;font-weight:800}
  .footer-bar .contact__web{color:var(--white)}
</style>
</head>
<body>

<section class="sheet sheet--front">
  <div class="brand"><span class="brand__mark"></span>NOVA FORGE</div>
  <div class="hero-photo" role="img" aria-label="Photo of a 3D printer nozzle printing a rubber part"></div>
  <svg class="hero-ring" viewBox="0 0 290 300" aria-hidden="true">
    <path d="M 40 150 A 110 110 0 1 1 145 260" fill="none" stroke="var(--charcoal)" stroke-width="14"/>
    <path d="M 145 260 A 110 110 0 0 1 55 210" fill="none" stroke="var(--orange)" stroke-width="14"/>
    <circle cx="40" cy="150" r="7" fill="var(--charcoal)"/>
  </svg>
  <div class="headline">
    <div class="headline__big">3D</div>
    <div class="headline__sub">PRINTING</div>
    <div class="headline__sub">SERVICES</div>
  </div>
  <div class="samples">
    <div class="sample" role="img" aria-label="Photo of a printed rubber part"></div>
    <div class="sample" role="img" aria-label="Photo of a printer at work"></div>
    <div class="sample" role="img" aria-label="Photo of printed components"></div>
    <div class="sample" role="img" aria-label="Photo of a finished model"></div>
  </div>
  <div class="features">
    <div class="feature">
      <span class="feature__icon"><svg width="18" height="18" viewBox="0 0 18 18"><circle cx="9" cy="9" r="7" fill="none" stroke="#fff" stroke-width="1.6"/><path d="M9 4v5l3 2" fill="none" stroke="#fff" stroke-width="1.6"/></svg></span>
      <span class="feature__text">Reduce time to market from weeks to hours</span>
    </div>
    <div class="feature">
      <span class="feature__icon"><svg width="18" height="18" viewBox="0 0 18 18"><path d="M3 9h12M10 4l5 5-5 5" fill="none" stroke="#fff" stroke-width="1.6"/></svg></span>
      <span class="feature__text">Create lightweight flexible parts</span>
    </div>
    <div class="feature">
      <span class="feature__icon"><svg width="18" height="18" viewBox="0 0 18 18"><rect x="3" y="3" width="12" height="12" fill="none" stroke="#fff" stroke-width="1.6"/><path d="M6 9l2 2 4-4" fill="none" stroke="#fff" stroke-width="1.6"/></svg></span>
      <span class="feature__text">Print on demand any volume</span>
    </div>
  </div>
  <div class="contact">
    <span class="contact__item"><svg width="14" height="14" viewBox="0 0 24 24"><path d="M6.6 10.8a15 15 0 0 0 6.6 6.6l2.2-2.2a1 1 0 0 1 1-.25 11.4 11.4 0 0 0 3.6.6 1 1 0 0 1 1 1V20a1 1 0 0 1-1 1A17 17 0 0 1 3 4a1 1 0 0 1 1-1h3.5a1 1 0 0 1 1 1c0 1.25.2 2.45.6 3.6a1 1 0 0 1-.25 1z" fill="var(--orange)"/></svg>+01-555-010-2040</span>
    <span class="contact__web">www.novaforge-print.com</span>
  </div>
</section>

<section class="sheet sheet--back">
  <div class="wide-photo" role="img" aria-label="Photo of a hand holding a printed rubber part"></div>
  <div class="intro">
    <h1 class="intro__title">Redefine your industry<br><span>with 3D PRINTING</span></h1>
    <p class="intro__copy">We print precise, durable rubber parts for prototypes and production runs. Our team turns your ideas into tested parts quickly, with steady quality and fair pricing for every order.</p>
  </div>
  <ul class="checklist">
    <li><svg width="8" height="8" viewBox="0 0 10 10"><path d="M1 5l3 3 5-6" fill="none" stroke="var(--orange)" stroke-width="2"/></svg>Flexible rubber prototypes in days</li>
    <li><svg width="8" height="8" viewBox="0 0 10 10"><path d="M1 5l3 3 5-6" fill="none" stroke="var(--orange)" stroke-width="2"/></svg>Short production runs on demand</li>
    <li><svg width="8" height="8" viewBox="0 0 10 10"><path d="M1 5l3 3 5-6" fill="none" stroke="var(--orange)" stroke-width="2"/></svg>Tough, skin-safe elastomer materials</li>
    <li><svg width="8" height="8" viewBox="0 0 10 10"><path d="M1 5l3 3 5-6" fill="none" stroke="var(--orange)" stroke-width="2"/></svg>Precise detail down to fine tolerances</li>
    <li><svg width="8" height="8" viewBox="0 0 10 10"><path d="M1 5l3 3 5-6" fill="none" stroke="var(--orange)" stroke-width="2"/></svg>Design support from our engineers</li>
    <li><svg width="8" height="8" viewBox="0 0 10 10"><path d="M1 5l3 3 5-6" fill="none" stroke="var(--orange)" stroke-width="2"/></svg>Fast shipping to your door</li>
  </ul>
  <h2 class="benefits__title">BENEFITS <span>OF 3D PRINTING</span></h2>
  <ul class="benefits">
    <li class="benefit">
      <span class="benefit__icon"><svg width="20" height="20" viewBox="0 0 20 20"><circle cx="10" cy="10" r="7" fill="none" stroke="var(--orange)" stroke-width="1.6"/><path d="M10 5v5l3 2" fill="none" stroke="var(--orange)" stroke-width="1.6"/></svg></span>
      <div><div class="benefit__title">SPEED TIME TO MARKET</div><p class="benefit__text">Move from design to a tested rubber part in days, not weeks, and launch sooner.</p></div>
    </li>
    <li class="benefit">
      <span class="benefit__icon"><svg width="20" height="20" viewBox="0 0 20 20"><path d="M3 10h14M12 5l5 5-5 5" fill="none" stroke="var(--orange)" stroke-width="1.6"/></svg></span>
      <div><div class="benefit__title">SPEED TIME TO MARKET</div><p class="benefit__text">Skip costly tooling and change your design freely between each new print run.</p></div>
    </li>
    <li class="benefit">
      <span class="benefit__icon"><svg width="20" height="20" viewBox="0 0 20 20"><rect x="4" y="4" width="12" height="12" fill="none" stroke="var(--orange)" stroke-width="1.6"/><path d="M7 10l2 2 4-4" fill="none" stroke="var(--orange)" stroke-width="1.6"/></svg></span>
      <div><div class="benefit__title">SPEED TIME TO MARKET</div><p class="benefit__text">Get soft, strong parts with complex shapes that molding simply cannot make.</p></div>
    </li>
    <li class="benefit">
      <span class="benefit__icon"><svg width="20" height="20" viewBox="0 0 20 20"><path d="M10 3l2 5h5l-4 3 2 5-5-3-5 3 2-5-4-3h5z" fill="none" stroke="var(--orange)" stroke-width="1.4"/></svg></span>
      <div><div class="benefit__title">SPEED TIME TO MARKET</div><p class="benefit__text">Order one part or thousands and pay only for what your project truly needs.</p></div>
    </li>
  </ul>
  <div class="footer-bar">
    <span class="contact__item"><svg width="13" height="13" viewBox="0 0 24 24"><path d="M6.6 10.8a15 15 0 0 0 6.6 6.6l2.2-2.2a1 1 0 0 1 1-.25 11.4 11.4 0 0 0 3.6.6 1 1 0 0 1 1 1V20a1 1 0 0 1-1 1A17 17 0 0 1 3 4a1 1 0 0 1 1-1h3.5a1 1 0 0 1 1 1c0 1.25.2 2.45.6 3.6a1 1 0 0 1-.25 1z" fill="#fff"/></svg>+01-555-010-2040</span>
    <span class="contact__web">www.novaforge-print.com</span>
  </div>
</section>

</body>
</html>
```